Training Company Needs a Web Design

We are a Training company that needs a website design completed for us. "The Harbor Loft" The website will be a 'community space' specialising in 'Change and Transformation'. It will be a 'space' where individuals can come to find out 'latest news', upcoming events and courses, chat with others and find 'tools and templates'. They will need to login as a 'Member'.

The final design needs to be professional but have a 'fun and interactive' feel and appeal to our target audience who are predominantly corporate individuals.

Target Market(s)

Corporate Individuals - they may have a Change or Project background

Industry/Entity Type

Business Consultant

Number of Pages Required

3 page

Font styles to use
Sans Serif

Requirements
Must have
• Design for 'Home Page'
• A professional and corporate 'feel' but be fun and interactive.
Nice to have
• A 'sense' of how some of the other pages may be designed or laid out.

```html
<!DOCTYPE html>
<html lang="en">
<head>
<meta charset="utf-8">
<title>The Harbor Loft – Home</title>
<link href="https://fonts.googleapis.com/css2?family=Open+Sans:wght@300;400;600;700&display=swap" rel="stylesheet">
<style>
:root{
  --blue:#0b4f96;
  --blue-mid:#1d5c9e;
  --blue-dark:#0a3f7a;
  --blue-light:#2f7fd0;
  --ink:#333;
  --grey:#777;
  --pale:#f1f2f4;
  --white:#fff;
  --black:#0a0a0a;
}
*{box-sizing:border-box;margin:0;padding:0}
html,body{width:1200px;height:4215px;overflow:hidden}
body{font-family:"Open Sans",Arial,sans-serif;color:var(--ink);background:var(--white)}
.page{position:relative;width:1200px;height:4215px;overflow:hidden}
section,header,footer{position:absolute;left:0;width:1200px}
.abs{position:absolute}
.btn{position:absolute;display:flex;align-items:center;justify-content:center;font-size:17px;letter-spacing:.5px;text-transform:uppercase}
.btn-blue{background:var(--blue);color:var(--white)}
.btn-white{background:var(--white);color:var(--blue)}
.heading{position:absolute;left:0;width:1200px;text-align:center;font-weight:400;font-size:40px;color:#3a3a3a;letter-spacing:.5px}
.heading b{font-weight:400;color:var(--blue)}
.subhead{position:absolute;left:0;width:1200px;text-align:center;font-size:16px;color:#999}
.photo{position:absolute}

/* header */
.site-header{top:0;height:140px;z-index:3}
.brand{position:absolute;left:84px;top:22px;display:flex;align-items:center;gap:14px;color:var(--blue-light);font-weight:400;font-size:26px;line-height:1.05;text-transform:uppercase}
.brand i{display:block;width:24px;height:24px;background:var(--blue-light)}
.nav{position:absolute;left:346px;top:64px;display:flex;gap:29px;font-size:14px;font-weight:600;color:#222;text-transform:uppercase}
.nav .active:after{content:"";display:block;margin:6px auto 0;width:0;height:0;border-left:6px solid transparent;border-right:6px solid transparent;border-top:7px solid var(--blue)}
.call{position:absolute;left:866px;top:24px;font-size:15px;color:var(--blue);display:flex;align-items:center;gap:8px}
.call span.dot{width:20px;height:20px;border-radius:50%;background:var(--blue-light)}
.login{position:absolute;left:1045px;top:52px;width:80px;height:42px;border:1px solid var(--blue);color:var(--blue);font-size:14px;font-weight:600;display:flex;align-items:center;justify-content:center}

/* hero */
.hero{top:0;height:717px}
.hero-photo{left:0;top:0;width:1200px;height:717px;background:linear-gradient(100deg,#7d8a95 0%,#b8c3cc 35%,#e9eef2 60%,#cdd3d9 100%)}
.hero-title{position:absolute;left:79px;top:392px;color:var(--white);font-size:52px;font-weight:400;line-height:1.28;text-transform:uppercase}

/* features */
.features{top:717px;height:261px;background:var(--blue);display:flex}
.feature{flex:1;display:flex;flex-direction:column;align-items:center;padding-top:60px;color:#7ea6d6;font-size:18px;text-align:center;line-height:1.2;border-right:1px solid #0f5aa5}
.feature.on{color:var(--white)}
.feature svg{margin-bottom:26px}

/* welcome */
.welcome{top:978px;height:469px}
.welcome p{position:absolute;left:174px;top:130px;width:854px;text-align:center;font-size:14px;line-height:30px;color:#666}

/* coaching */
.coaching{top:1447px;height:492px}
.coach-bg{left:0;top:0;width:1200px;height:492px;background:linear-gradient(180deg,#e6eaee 0%,#d3d9df 55%,#b9c1c9 100%)}
.card{position:absolute;top:169px;width:384px;height:213px;background:#111;border:3px solid #3a3a3a}
.card .pic{position:absolute;top:14px;width:150px;height:183px}
.card h4{position:absolute;top:14px;font-size:16px;font-weight:400;color:#ddd;text-transform:uppercase}
.card p{position:absolute;top:64px;width:190px;font-size:14px;line-height:1.35;color:#aaa}
.card .social{position:absolute;top:166px;display:flex;gap:10px}
.card .social i{width:16px;height:16px;border-radius:50%;border:1.5px solid #aaa}

/* events */
.events{top:1939px;height:492px;background:linear-gradient(160deg,#f6f6f7,#e6e7e9)}
.event-date{position:absolute;left:100px;top:62px;color:#fff;font-size:14px}
.event-title{position:absolute;left:100px;top:88px;color:#fff;font-size:26px}

/* testimonials */
.testimonials{top:2431px;height:402px}
.testi-box{position:absolute;left:143px;top:154px;width:914px;height:132px;background:#eeeeef}
.testi-box p{position:absolute;left:90px;top:28px;width:734px;text-align:center;font-size:14px;line-height:31px;color:#333}
.arrow{position:absolute;top:0;width:40px;height:132px;background:var(--blue);color:#fff;display:flex;align-items:center;justify-content:center;font-size:22px;font-weight:700}
.client{position:absolute;left:444px;top:275px;width:315px;height:62px;background:#fff;border:1px solid #e3e3e3;display:flex;align-items:center;justify-content:center;font-size:14px;font-weight:700;text-transform:uppercase}

/* news */
.news{top:2833px;height:435px;background:var(--blue-mid)}
.news .heading{color:#0c1a2c}
.news .heading b{color:#fff}
.news-item{position:absolute;top:151px;width:330px;height:130px}
.date{position:absolute;left:0;top:0;width:82px;height:90px;background:#fff}
.date strong{display:block;height:54px;text-align:center;font-size:38px;line-height:54px;color:#111;font-weight:600}
.date span{display:block;height:36px;background:var(--black);color:#fff;text-align:center;font-size:22px;line-height:36px}
.news-item h5{position:absolute;left:105px;top:0;width:225px;font-size:15px;font-weight:400;color:#fff;line-height:1.35}
.news-item p{position:absolute;left:105px;top:50px;width:215px;font-size:14px;color:#0d1f35;line-height:1.45}

/* contact */
.contact{top:3268px;height:520px}
.contact .intro{position:absolute;left:200px;top:132px;width:800px;text-align:center;font-size:14px;line-height:30px;color:#666}
.field{position:absolute;left:126px;width:470px;height:42px;border:1px solid var(--blue);padding:0 12px;font-size:13px;line-height:40px;color:#555}
.field.filled{background:var(--blue);color:#fff}
.message{position:absolute;left:604px;top:208px;width:467px;height:166px;border:1px solid var(--blue);padding:8px 12px;font-size:13px;color:#555}

/* footer */
.site-footer{top:3788px;height:365px;background:var(--blue)}
.col-title{position:absolute;top:62px;width:220px;text-align:center;color:#fff;font-size:18px;text-transform:uppercase;padding-bottom:10px;border-bottom:1px solid #3f78b4}
.foot-brand{position:absolute;left:79px;top:128px;display:flex;align-items:center;gap:12px;color:#fff;font-size:26px;line-height:1.05;text-transform:uppercase}
.foot-brand i{display:block;width:24px;height:24px;background:#fff}
.foot-about{position:absolute;left:79px;top:240px;width:216px;font-size:14px;line-height:1.5;color:#fff}
.foot-nav{position:absolute;left:353px;top:118px;display:grid;grid-template-columns:104px 104px;row-gap:22px;font-size:13px;color:#fff;text-transform:uppercase}
.foot-nav .cur{text-decoration:underline}
.foot-input{position:absolute;left:616px;width:215px;height:42px;border:1px solid #fff;color:#fff;font-size:14px;line-height:40px;padding:0 10px}
.hex{position:absolute;top:108px}
.copyright{top:4153px;height:62px;background:var(--black);color:#fff;font-size:13px;display:flex;align-items:center;justify-content:center}
</style>
</head>
<body>
<div class="page">

  <section class="hero">
    <div class="photo hero-photo" role="img" aria-label="Photo of a smiling businesswoman in front of a team meeting in a bright office"></div>
    <h1 class="hero-title">Progressive Business<br>Thinking</h1>
    <div class="btn btn-blue" style="left:81px;top:543px;width:209px;height:61px">Contact Now</div>
  </section>

  <header class="site-header">
    <div class="brand"><i></i><span>The<br>Harbor Loft</span></div>
    <div class="call"><span>CALL :</span><span class="dot"></span><span>+0100 555 0199 FREE</span></div>
    <nav class="nav">
      <span class="active">Home</span><span>About</span><span>Services</span><span>Event</span><span>News</span><span>Coaching</span><span>Courses</span><span>Contact</span>
    </nav>
    <div class="login">LOGIN</div>
  </header>

  <section class="features">
    <div class="feature on">
      <svg width="56" height="56" viewBox="0 0 56 56"><rect x="6" y="24" width="10" height="24" fill="#fff"/><path d="M20 24 L30 8 Q36 8 34 18 L46 18 Q52 20 49 27 L44 46 Q42 48 38 48 L20 48 Z" fill="#fff"/></svg>
      Lorem Ipsum is<br>simply
    </div>
    <div class="feature">
      <svg width="56" height="56" viewBox="0 0 56 56"><circle cx="24" cy="24" r="13" fill="none" stroke="#7ea6d6" stroke-width="4"/><line x1="34" y1="34" x2="48" y2="48" stroke="#7ea6d6" stroke-width="5"/></svg>
      Lorem Ipsum is<br>simply
    </div>
    <div class="feature">
      <svg width="56" height="56" viewBox="0 0 56 56" fill="none" stroke="#7ea6d6" stroke-width="3"><circle cx="18" cy="20" r="9"/><circle cx="38" cy="20" r="9"/><path d="M6 40 L50 32"/><line x1="28" y1="36" x2="28" y2="50"/><line x1="18" y1="50" x2="38" y2="50"/></svg>
      Lorem Ipsum is<br>simply
    </div>
    <div class="feature" style="border-right:none">
      <svg width="56" height="56" viewBox="0 0 56 56" fill="none" stroke="#7ea6d6" stroke-width="5" stroke-dasharray="5 3"><circle cx="22" cy="30" r="11"/><circle cx="42" cy="16" r="7"/></svg>
      Lorem Ipsum is<br>simply
    </div>
  </section>

  <section class="welcome">
    <h2 class="heading" style="top:60px">WELCOME TO <b>THE HARBOR LOFT</b></h2>
    <p>Lorem Ipsum is simply dummy text of the printing and typesetting industry. Lorem Ipsum has been the industry's standard dummy text ever since the 1500s, when an unknown printer took a galley of type and scrambled it to make a type specimen book. It has survived not only five centuries, but also the leap into electronic typesetting, remaining essentially unchanged. It was popularised in the 1960s with the release of Letraset sheets containing Lorem Ipsum passages, and more recently with desktop publishing software like Aldus PageMaker including versions of Lorem Ipsum. It is a long established fact that a reader will be distracted by the readable content of a page when looking at its layout. The point of using Lorem Ipsum is that it has a more-or-less normal distribution of letters, as opposed to using 'Content here, content here', making it look like readable English.</p>
    <div class="btn btn-blue" style="left:514px;top:342px;width:169px;height:63px">Read More</div>
  </section>

  <section class="coaching">
    <div class="photo coach-bg" role="img" aria-label="Soft-focus photo of hands typing on a laptop keyboard"></div>
    <h2 class="heading" style="top:62px;color:var(--blue)">COACHING</h2>
    <div class="subhead" style="top:112px;font-size:14px;color:#666">BEST MEMBER OF COACHES</div>
    <div class="card" style="left:208px">
      <div class="pic" role="img" aria-label="Photo of a smiling group of students" style="left:14px;background:linear-gradient(160deg,#b9a58c,#8d3b3b)"></div>
      <h4 style="left:182px">Nora Whitfield</h4>
      <div class="abs" style="left:182px;top:44px;width:180px;height:1px;background:#444"></div>
      <p style="left:182px">Lorem Ipsum is simply dummy text of the printing and typesetting industry. Lorem Ipsum has been...</p>
      <div class="social" style="left:182px"><i></i><i></i><i></i><i></i><i></i></div>
    </div>
    <div class="card" style="left:607px">
      <h4 style="left:84px">Daniel Brooke</h4>
      <div class="abs" style="left:14px;top:44px;width:190px;height:1px;background:#444"></div>
      <p style="left:14px">Lorem Ipsum is simply dummy text of the printing and typesetting industry. Lorem Ipsum has been...</p>
      <div class="social" style="left:34px"><i></i><i></i><i></i><i></i><i></i></div>
      <div class="pic" role="img" aria-label="Photo of a coach in front of a green chalkboard" style="left:216px;background:linear-gradient(160deg,#5f8a5a,#e9e4dc)"></div>
    </div>
  </section>

  <section class="events">
    <h2 class="heading" style="top:62px">LATEST <b>EVENT</b></h2>
    <div class="subhead" style="top:114px">Lorem Ipsum is simply dummy text of the printing</div>
    <div class="photo" role="img" aria-label="Darkened photo of a business meeting around a table" style="left:79px;top:169px;width:331px;height:219px;background:linear-gradient(135deg,#3a3a3a,#6b6b6b)">
      <div class="event-date">February 22, 2016</div>
      <div class="event-title">Lorem ipsum</div>
      <div class="btn btn-white" style="left:92px;top:135px;width:147px;height:52px;font-size:16px">Read More</div>
    </div>
    <div class="photo" role="img" aria-label="Photo of a presenter speaking to a seated audience" style="left:430px;top:169px;width:337px;height:219px;background:linear-gradient(135deg,#c9ccd1,#7f8893)"></div>
    <div class="photo" role="img" aria-label="Photo of a workshop group seated at a conference table" style="left:790px;top:169px;width:331px;height:219px;background:linear-gradient(135deg,#d4d0cc,#6c6a78)"></div>
  </section>

  <section class="testimonials">
    <h2 class="heading" style="top:56px">OUR <b>TESTIMONIALS</b></h2>
    <svg class="abs" style="left:565px;top:118px" width="70" height="56" viewBox="0 0 70 56"><path d="M4 56 V28 Q4 6 28 0 V12 Q16 16 16 26 H30 V56 Z M40 56 V28 Q40 6 64 0 V12 Q52 16 52 26 H66 V56 Z" fill="#444"/></svg>
    <div class="testi-box">
      <div class="arrow" style="left:0">«</div>
      <p>Lorem Ipsum is simply dummy text of the printing and typesetting industry. Lorem Ipsum has been the industry's standard dummy text ever since the 1500s, when an unknown printer took a galley of type and scrambled it to make a type specimen book. It has survived not only five centuries, but also the leap into electronic typesetting...</p>
      <div class="arrow" style="right:0">»</div>
    </div>
    <div class="client">Client Name</div>
  </section>

  <section class="news">
    <h2 class="heading" style="top:62px">LATEST <b>NEWS</b></h2>
    <div class="news-item" style="left:81px">
      <div class="date"><strong>21</strong><span>Feb</span></div>
      <h5>Lorem Ipsum is simply dummy text of</h5>
      <p>Lorem Ipsum is simply dummy text of Lorem Ipsum is simply dummy text of ....</p>
    </div>
    <div class="news-item" style="left:446px">
      <div class="date"><strong>20</strong><span>Feb</span></div>
      <h5>Lorem Ipsum is simply dummy text of</h5>
      <p>Lorem Ipsum is simply dummy text of Lorem Ipsum is simply dummy text of ....</p>
    </div>
    <div class="news-item" style="left:810px">
      <div class="date"><strong>19</strong><span>Feb</span></div>
      <h5>Lorem Ipsum is simply dummy text of</h5>
      <p>Lorem Ipsum is simply dummy text of Lorem Ipsum is simply dummy text of ....</p>
    </div>
    <div class="btn btn-white" style="left:517px;top:311px;width:166px;height:59px">Show All</div>
  </section>

  <section class="contact">
    <h2 class="heading" style="top:62px">OUR <b>CONTACT</b></h2>
    <p class="intro">Lorem Ipsum is simply dummy text of the printing and typesetting industry. Lorem Ipsum has been the industry's standard dummy text ever since the 1500s</p>
    <div class="field filled" style="top:208px">Name*</div>
    <div class="field" style="top:270px">Email*</div>
    <div class="field" style="top:332px">Phone*</div>
    <div class="message">Message*</div>
    <div class="btn btn-blue" style="left:517px;top:393px;width:166px;height:62px">Submit</div>
  </section>

  <footer class="site-footer">
    <div class="col-title" style="left:79px">About</div>
    <div class="foot-brand"><i></i><span>The<br>Harbor Loft</span></div>
    <p class="foot-about">Lorem ipsum dolor sit amet, consectetur elit. Lorem ipsum Elit..</p>

    <div class="col-title" style="left:343px">Navigation</div>
    <div class="foot-nav">
      <span class="cur">Home</span><span>News</span>
      <span>About</span><span>Coaching</span>
      <span>Services</span><span>Courses</span>
      <span>Event</span><span>Contact</span>
    </div>

    <div class="col-title" style="left:613px">Newsletter</div>
    <div class="foot-input" style="top:130px">User Name*</div>
    <div class="foot-input" style="top:185px">Email*</div>
    <div class="btn btn-white" style="left:616px;top:246px;width:215px;height:50px;font-size:16px">Subscribe</div>

    <div class="col-title" style="left:894px">Follow Us</div>
    <svg class="hex" style="left:893px" width="60" height="64" viewBox="0 0 60 64"><polygon points="30,2 57,17 57,47 30,62 3,47 3,17" fill="none" stroke="#fff" stroke-width="2"/><polygon points="30,10 50,21 50,43 30,54 10,43 10,21" fill="#fff" opacity=".15"/></svg>
    <svg class="hex" style="left:975px" width="60" height="64" viewBox="0 0 60 64"><polygon points="30,2 57,17 57,47 30,62 3,47 3,17" fill="none" stroke="#fff" stroke-width="2"/><polygon points="30,10 50,21 50,43 30,54 10,43 10,21" fill="#fff" opacity=".15"/></svg>
    <svg class="hex" style="left:1057px" width="60" height="64" viewBox="0 0 60 64"><polygon points="30,2 57,17 57,47 30,62 3,47 3,17" fill="none" stroke="#fff" stroke-width="2"/><polygon points="30,10 50,21 50,43 30,54 10,43 10,21" fill="#fff" opacity=".15"/></svg>
  </footer>

  <div class="copyright" style="position:absolute;left:0;width:1200px">Copyright 2016&nbsp;<strong>THE HARBOR LOFT</strong>&nbsp;All rights reserved</div>
</div>
</body>
</html>
```